Board menu for "Pan Dorado" food truck

Summary
**********************************
We need a menu design for a food truck. The menu will be printed and placed in the food truck side, so that customers can read it while standing one or two meters away from it. The size of the printed menu should be (width x height): 108cm x 70cm. The food truck is located in Panama and the menu language is Spanish.

Menu Sections
**************************************
The menu is divided in the following 5 sections:

1. Main Courses: This section should take most of the menu space. There are 5 menu items in this section. Each item has a Name, Description, Picture, Price (of item alone), and Price (of item in combo). Please note that for all items, combo means adding one beverage and one side. The added price is $1.50 to make any main course a combo. So it might we better to say “make it a combo for +$1.50” versus say “alone $5.50, in combo $7.00”.

2. Side Orders: This section has 2 menu items. Each item has a Name and Price. There are no pictures for this section or items.

3. Soups: This section has a Picture and Description for the entire section plus 2 menu items. Each menu item has a Name and Price.

4. Bakery: This section has a Picture for the entire section plus 5 menu items. Each item has a Name and a Price.

5. Beverages: This section has 5 menu items. Each menu item has a Name and a Price. There are no pictures for this section or items.

Attachments
*******************************************
We are attaching a zip file with picture of the exterior of the food truck. The menu will go in the space between the food truck’s window and the light switch, leaving ample space between those boundaries and the menu. The trash can shown in the picture has been relocated so it will not obstruct the menu view.

The zip file also contains the pictures for the 5 menu items in the Main Courses section, the picture for the Soups section, and the picture for the Bakery section (the bakery picture is provided as a place holder. We will provide a better bakery picture to the winning design to replace this one). For information purposes, the zip file also contains the food truck logo. The logo will not go in the menu. The brand and social media icons will go elsewhere in the truck.

The zip file also contains the file “menu information.xlsx”. This file has the following sheets:

Sections: Contains a column with the section name in English and another one with the section name in Spanish (which should be used in the menu). For the Soups section, contains a column with the section’s Description and Picture Name. For the Bakery section, contains a column with the section’s Picture Name.

Main Courses: Contains a column for each of the following: Item Name, Item Description, Item Picture Name, Item Price, Item Price (in combo). Again, we leave it to the designer’s discretion to use +$1.50 (or similar) for the combo versus publishing the full combo price.

Side Orders: Contains columns for Item Name and Item Price.

Soups: Contains columns for Item Name and Item Price.

Bakery: Contains columns for Item Name and Item Price. In the case of the Donuts item, there is an addition column with the Available Flavors.

Beverages: Contains columns for Item Name and Item Price. In the case of the Sodas item, there is an additional column with the Available Flavors.

A note about file encoding: the excel file contains texts with Spanish language special characters. It is encoded in the Windows-1252 encoding which I think is the Excel default for Western European languages. For those having trouble with this encoding, I included a “menu information csv” folder in the zip file with all the sheets in csv format encoded using UTF-8.
Updates

Target Market(s)

The truck sells fast food to drivers commuting from Panama City to towns in the west of the city. The average customer is a middle-class professional with a car. The truck is located in one of our gas stations so most customers stop to fuel their cars and grab something to eat for the ride home.

Font styles to use
Sans Serif

Colors

Designer to choose colors to be used in the design.

Requirements
Must have
• We would like to make emphasis in the main courses. Since they required preparation, they are not displayed, unlike other items like bakery, soups and beverages that are always ready and displayed. Having their pictures and descriptions on the menu will allows the customer to quickly figure out what main courses are available.

```html
<!DOCTYPE html>
<html lang="es">
<head>
<meta charset="utf-8">
<title>Pan Dorado — Menú</title>
<link rel="stylesheet" href="https://fonts.googleapis.com/css2?family=Bebas+Neue&family=Arimo:ital,wght@0,400;0,700;1,400&display=swap">
<style>
  :root{
    --page:#e9e6e1;
    --board-dark:#0d0d0d;
    --board-mid:#1c1c1c;
    --ink:#ffffff;
    --ink-soft:#d9d9d9;
    --accent:#e31e24;
    --rule:#bdbdbd;
    --photo-sandwich:linear-gradient(135deg,#c98a4b,#e7c9a0 55%,#c8383a);
    --photo-pastry:radial-gradient(ellipse at center,#d99a45 0%,#b8742a 55%,rgba(0,0,0,0) 75%);
    --photo-soup:linear-gradient(160deg,#f4f1e8,#e6cf7a 55%,#d2262e);
  }
  *{margin:0;padding:0;box-sizing:border-box}
  html,body{width:1200px;height:1200px;overflow:hidden}
  body{background:var(--page);font-family:"Arimo",Arial,sans-serif;color:var(--ink)}
  .menu{position:absolute;left:30px;top:229px;width:1140px;height:742px;
    background:linear-gradient(90deg,var(--board-dark),var(--board-mid) 50%,var(--board-dark));overflow:hidden}
  .menu > *{position:absolute}
  .heading{font-family:"Bebas Neue",Arial Narrow,sans-serif;font-weight:400;color:var(--ink);line-height:.95}
  .heading--main{left:87px;top:31px;font-size:60px;letter-spacing:1px}
  .heading--bakery{left:464px;width:272px;top:50px;font-size:50px;text-align:center;letter-spacing:1px}
  .heading--sides{left:786px;width:323px;top:34px;font-size:44px;text-align:center;letter-spacing:10px;line-height:.92}
  .heading--drinks{left:786px;width:323px;top:238px;font-size:46px;text-align:center;letter-spacing:1px}
  .heading--soups{left:700px;width:189px;top:562px;font-size:46px;text-align:right;letter-spacing:1px}

  .photo{border-radius:4px}
  .photo--dish{left:0;width:139px;height:84px;background:var(--photo-sandwich)}
  .photo--pastry{left:482px;top:386px;width:234px;height:142px;background:var(--photo-pastry)}
  .photo--soup{left:965px;top:564px;width:175px;height:178px;background:var(--photo-soup);border-radius:10px 0 0 0}

  .dish{left:149px;width:264px}
  .dish__name{font-weight:700;font-size:16.5px;color:var(--accent);line-height:1}
  .dish__desc{font-size:7.6px;line-height:1.4;text-transform:uppercase;width:205px;margin-top:2px;color:var(--ink-soft)}
  .dish__price{position:absolute;right:0;top:-8px;text-align:right;width:60px}
  .price-solo{color:var(--accent);font-weight:700;display:flex;justify-content:flex-end;align-items:flex-start;line-height:1}
  .price-solo .cur{font-size:15px;margin-top:3px}
  .price-solo .big{font-size:33px;letter-spacing:-1px}
  .price-solo .cents{display:flex;flex-direction:column;align-items:center;font-size:15px;margin-top:2px}
  .price-solo .cents small{font-size:5px;color:var(--ink);letter-spacing:.3px}
  .price-combo{font-size:9.5px;font-weight:700;line-height:1;margin-top:1px}
  .price-combo small{display:block;font-size:5px;letter-spacing:.3px}
  .rule{height:1px;background:var(--rule)}
  .rule--dish{left:149px;width:264px}

  .footnote{left:18px;top:721px;font-size:6.4px;font-style:italic;color:var(--ink-soft)}
  .footnote b{font-style:italic}

  .list{list-style:none}
  .list li{display:flex;justify-content:space-between;flex-wrap:wrap;font-weight:700;font-size:15px;height:44.5px;padding-top:6px;border-bottom:1px solid var(--rule)}
  .list li:last-child{border-bottom:none}
  .list .note{flex-basis:100%;font-weight:400;font-style:italic;font-size:10px;margin-top:3px}
  .list--bakery{left:464px;width:272px;top:132px}
  .list--sides{left:786px;width:323px;top:132px}
  .list--drinks{left:786px;width:323px;top:301px}
  .list--drinks li.tall{height:60px}
  .list--soups{left:464px;width:425px;top:642px}
  .soups__desc{left:560px;width:329px;top:605px;text-align:right;font-size:10.5px;font-style:italic}
</style>
</head>
<body>
<main class="menu">
  <h2 class="heading heading--main">Platos<br>Principales</h2>

  <div class="photo photo--dish" style="top:181px" role="img" aria-label="Sándwich de jamón y queso sobre papel a cuadros rojo y blanco"></div>
  <div class="photo photo--dish" style="top:294px" role="img" aria-label="Choripán con chimichurri y papas fritas"></div>
  <div class="photo photo--dish" style="top:407px" role="img" aria-label="Patacones con pollo y salsa de ajo"></div>
  <div class="photo photo--dish" style="top:520px" role="img" aria-label="Emparedado de pollo en pan baguette"></div>
  <div class="photo photo--dish" style="top:616px" role="img" aria-label="Hamburguesa con papas fritas"></div>

  <article class="dish" style="top:204px">
    <h3 class="dish__name">A LA PEÑA</h3>
    <p class="dish__desc">Emparedado de queso americano y jamones variados en pan flauta, a la peña.</p>
    <div class="dish__price"><div class="price-solo"><span class="cur">$</span><span class="big">2</span><span class="cents">50<small>SOLO</small></span></div><div class="price-combo">$4.00<small>COMBO</small></div></div>
  </article>
  <div class="rule rule--dish" style="top:255px"></div>

  <article class="dish" style="top:319px">
    <h3 class="dish__name">BUCOPOCOTÓN</h3>
    <p class="dish__desc">Choripan de chorizo criollo jumbo con chimichurri de la casa en pan baguette.</p>
    <div class="dish__price"><div class="price-solo"><span class="cur">$</span><span class="big">3</span><span class="cents">00<small>SOLO</small></span></div><div class="price-combo">$4.50<small>COMBO</small></div></div>
  </article>
  <div class="rule rule--dish" style="top:370px"></div>

  <article class="dish" style="top:429px">
    <h3 class="dish__name">MI PATACÓN</h3>
    <p class="dish__desc">Pollo, cebolla caramelizada y salsa de ajo con cilantro sobre cama de patacones.</p>
    <div class="dish__price"><div class="price-solo"><span class="cur">$</span><span class="big">3</span><span class="cents">25<small>SOLO</small></span></div><div class="price-combo">$4.75<small>COMBO</small></div></div>
  </article>
  <div class="rule rule--dish" style="top:477px"></div>

  <article class="dish" style="top:531px">
    <h3 class="dish__name">EL FAVORITO</h3>
    <p class="dish__desc">Emparedado de pollo a la plancha, queso mozzarella, cebolla caramelizada, tomate y salsa ranch en pan baguette.</p>
    <div class="dish__price"><div class="price-solo"><span class="cur">$</span><span class="big">4</span><span class="cents">50<small>SOLO</small></span></div><div class="price-combo">$6.00<small>COMBO</small></div></div>
  </article>
  <div class="rule rule--dish" style="top:585px"></div>

  <article class="dish" style="top:638px">
    <h3 class="dish__name">LA BOCHINCHOSA</h3>
    <p class="dish__desc">1/2 libra de hamburguesa angus, queso americano, cebolla caramelizada, tomate, bacon y salsa de la casa en pan de miel con semillas de amapola.</p>
    <div class="dish__price"><div class="price-solo"><span class="cur">$</span><span class="big">5</span><span class="cents">50<small>SOLO</small></span></div><div class="price-combo">$7.00<small>COMBO</small></div></div>
  </article>

  <p class="footnote">* Por solo $1.50 convierte tu plato principal en <b>COMBO</b> – añadiendo una <b>CHICHA, SODA o AGUA</b> y un <b>ACOMPAÑAMIENTO</b>.</p>

  <h2 class="heading heading--bakery">Pastelería</h2>
  <ul class="list list--bakery">
    <li><span>Enchilada de Carne</span><span>$1.50</span></li>
    <li><span>Pastelito de Pollo</span><span>$1.25</span></li>
    <li><span>Pañuelo de Queso</span><span>$1.00</span></li>
    <li><span>Cañón de Guayaba</span><span>$0.85</span></li>
    <li><span>Donas Rellenas</span><span>$0.85</span><span class="note">Crema Pastelera, Fresa, Manzana, Maracuyá</span></li>
  </ul>
  <div class="photo photo--pastry" role="img" aria-label="Surtido de pastelitos horneados"></div>

  <h2 class="heading heading--sides">Acompaña<br>mientos</h2>
  <ul class="list list--sides">
    <li><span>Papas Fritas</span><span>$1.00</span></li>
    <li><span>Patacones</span><span>$1.00</span></li>
  </ul>

  <h2 class="heading heading--drinks">Bebidas</h2>
  <ul class="list list--drinks">
    <li><span>Chicheme Chorrerano (16oz)</span><span>$1.60</span></li>
    <li><span>Chicha del día (16oz)</span><span>$1.00</span></li>
    <li class="tall"><span>Sodas (12oz)</span><span>$1.00</span><span class="note">Cola Roja, Cola Cero, Toronjita, Brisa Fresa, Brisa Manzana</span></li>
    <li><span>Agua (16oz)</span><span>$0.75</span></li>
    <li><span>Café de Altura (8oz)</span><span>$1.00</span></li>
  </ul>

  <h2 class="heading heading--soups">Sopas</h2>
  <p class="soups__desc">12 onzas de sopa del día servida con 4 onzas de arroz blanco.</p>
  <ul class="list list--soups">
    <li><span>Sopa de Pollo con Arroz</span><span>$2.95</span></li>
    <li><span>Sopa de Lenteja y Carne con Arroz</span><span>$2.95</span></li>
  </ul>
  <div class="photo photo--soup" role="img" aria-label="Vaso de sopa de pollo con cuchara sobre papel a cuadros"></div>
</main>
</body>
</html>
```